Harborline Motors LLC

Car Dealer Customer Service
Address: 2741 Linden Avenue, Shelbyville, TN 37162
web: www.harborlinemotorstn.net
email: harborlinemotorstn@mailbox-example.net
Phone: (931) 555-0148
Phone: (629) 555-0173

```html
<!DOCTYPE html>
<html lang="en">
<head>
<meta charset="utf-8">
<title>Harborline Motors LLC – Business Card</title>
<link rel="stylesheet" href="https://fonts.googleapis.com/css2?family=Arimo:wght@400;700&display=swap">
<style>
  :root {
    --stage: #2a2a2a;
    --card-white: #ffffff;
    --brand-blue: #1f79ad;
    --brand-gold: #eab545;
    --ink-white: #ffffff;
  }
  * { box-sizing: border-box; margin: 0; padding: 0; }
  html, body { width: 1200px; height: 900px; overflow: hidden; }
  body {
    background: var(--stage);
    font-family: "Arimo", Arial, sans-serif;
    position: relative;
  }
  .card {
    position: absolute;
    width: 600px;
    height: 343px;
    left: 300px;
    border-radius: 4px;
    overflow: hidden;
  }
  .card-front { top: 88px; background: var(--card-white); }
  .card-back { top: 469px; background: var(--brand-blue); color: var(--ink-white); }

  .brand {
    position: absolute;
    left: 0; right: 0; top: 110px;
    display: flex; flex-direction: column; align-items: center;
  }
  .brand-name {
    display: flex; align-items: center; gap: 14px;
    color: var(--brand-blue);
    font-weight: 700;
    font-size: 40px;
    letter-spacing: 0.5px;
    text-transform: uppercase;
  }
  .brand-dot {
    width: 34px; height: 34px; border-radius: 50%;
    background: var(--brand-gold);
  }
  .brand-tagline {
    margin-top: 8px;
    color: var(--brand-gold);
    font-weight: 700;
    font-size: 17px;
    letter-spacing: 0.6px;
    text-transform: uppercase;
  }

  .address {
    position: absolute; left: 0; right: 0; top: 30px;
    text-align: center;
    font-weight: 700; font-size: 21px; line-height: 1.3;
    letter-spacing: 0.5px;
  }
  .address svg { display: block; margin: 0 auto 8px; }
  .phone-band {
    position: absolute; left: 0; right: 0; top: 152px; height: 50px;
    background: var(--brand-gold);
    display: flex; align-items: center; justify-content: center; gap: 12px;
    font-weight: 700; font-size: 28px; letter-spacing: 1px;
  }
  .contact-list {
    position: absolute; left: 0; right: 0; top: 228px;
    list-style: none;
    display: flex; flex-direction: column; align-items: center; gap: 12px;
    font-weight: 700; font-size: 19px; letter-spacing: 0.5px;
  }
  .contact-list li { display: flex; align-items: center; gap: 8px; }
  .icon { flex: none; }
</style>
</head>
<body>
  <section class="card card-front" aria-label="Card front">
    <div class="brand">
      <div class="brand-name"><span class="brand-dot"></span>Harborline Motors</div>
      <div class="brand-tagline">Car Dealer Customer Service</div>
    </div>
  </section>

  <section class="card card-back" aria-label="Card back">
    <div class="address">
      <svg class="icon" width="22" height="22" viewBox="0 0 24 24" aria-hidden="true">
        <circle cx="12" cy="12" r="11" fill="none" stroke="#fff" stroke-width="1.5"/>
        <path d="M12 5a4.5 4.5 0 0 0-4.5 4.5C7.5 13 12 18 12 18s4.5-5 4.5-8.5A4.5 4.5 0 0 0 12 5zm0 6.2a1.7 1.7 0 1 1 0-3.4 1.7 1.7 0 0 1 0 3.4z" fill="#fff"/>
      </svg>
      2741 Linden Avenue, Shelbyville,<br>TN 37162
    </div>

    <div class="phone-band">
      <svg class="icon" width="30" height="30" viewBox="0 0 24 24" aria-hidden="true">
        <circle cx="12" cy="12" r="11" fill="none" stroke="#fff" stroke-width="1.6"/>
        <path d="M9.2 6.5l1.3 2.6-1.1 1.2c.6 1.5 1.8 2.7 3.3 3.3l1.2-1.1 2.6 1.3-.6 2c-4.3.2-8.8-4.3-8.6-8.6z" fill="#fff"/>
      </svg>
      <span>(931) 555-0148 / (629) 555-0173</span>
    </div>

    <ul class="contact-list">
      <li>
        <svg class="icon" width="22" height="22" viewBox="0 0 24 24" aria-hidden="true">
          <circle cx="12" cy="12" r="11" fill="#fff"/>
          <g fill="none" stroke="#1f79ad" stroke-width="1.3">
            <circle cx="12" cy="12" r="6.5"/>
            <ellipse cx="12" cy="12" rx="3" ry="6.5"/>
            <path d="M5.5 12h13M6.5 8.8h11M6.5 15.2h11"/>
          </g>
        </svg>
        <span>www.harborlinemotorstn.net</span>
      </li>
      <li>
        <svg class="icon" width="22" height="22" viewBox="0 0 24 24" aria-hidden="true">
          <circle cx="12" cy="12" r="11" fill="#fff"/>
          <rect x="6" y="8" width="12" height="8.5" fill="none" stroke="#1f79ad" stroke-width="1.4"/>
          <path d="M6 8l6 5 6-5" fill="none" stroke="#1f79ad" stroke-width="1.4"/>
        </svg>
        <span>harborlinemotorstn@mailbox-example.net</span>
      </li>
    </ul>
  </section>
</body>
</html>
```